Ironpeak | Minimalist 6-panel Brochure

Background: Ironpeak Fabrication Corp. is a manufacturer of steel wire-based products (e.g. nails, galvanized wire, barbed wire, steel matting) in Manila.

Brand Differentiator: Uncompromising "first world" quality to push our "third world" country to develop

Customers: We are a B2B company - we supply the materials to be used by Contractors in building projects. Retailers in selling to home users,Wholesalers in distributing to their retailer networks.

Brochure Objective: Using a standard 6-panel 8.5" x 11" Brochure, to create awareness among contractors and in the architectural community as a leader in quality products and honest service. (architects are big influencers of contractors in that they can recommend quality suppliers to them)

Brochure Contents: I have attached (in Powerpoint) the copy points of the Brochures broken down by 6 panels of content.
**DO NOT MIND how I've layout-ed the info in the .ppt, It's for your easier understanding only**

Brand Essence to Consider: 'First-world' in terms of product standards. Transparent & honest in terms of service/delivery. Approachable from Big to Small customers.

*Bonus Brand Essence: Someone you can have a 'light' conversation with over the phone for a quotation.*

Design Guidelines:
1) Be creative. If you think any of the guidelines I mention below won't be the best fit to your interpretation of my vision, go ahead and do what you think is best!

2) Be minimalist. I've kept the copy points's words at a minimum so there would be more emphasis on the content. Design around the copy points that bring out the gist more and the details less.

3) Design flat. Make the design look simple yet attractive.
PEG: If there was a website that I'd like to take design cues from, it's www.velorant.com and brindlepay.com/purse . Details like font size, font color, etc here were nicely differentiated for Headers, Subtexts and Descriptions. Be playful with using font effects like BOLD and Italics.

4) Use Icons. Instead of using a photo-heavy brochure, it would be better if we created icons for the brochure parts ('Our Thinking', 'How We Serve You', 'How It Works')
PEG: Abstract/minimalist icons such as those seen at the top of tovimark.com or the middle section of quillardent.com would be nice.

5) Edit the Product Shots and Pics of our Tech/Machines. Kindly edit and 'beautify' the photos attached to align to your design. Use 1 shot per product. Some are in .jpeg and some in .psd. (see attached. remove the watermarks in .psd shots)

6) Fit the Logo. Feel free to change to color schemes of our logo to make it fit with your designs. (see attached)

7) Front Cover. Kindly go through our 'Tagline' and 'Short Overall Description' first to find inspiration for some simple artwork.
*sidenote: For you to understand our tagline, the Philippines hasn't fully developed a priority for quality in terms of steel materials used in construction. (price had always dictated the market) And we want to help push them to that point in shaping the country's real estate development from 3rd world to a 1st world country's standards.

8) Word Cloud. I've listed 8 of the biggest and well-known projects we've supported in the past 5 years in 'Supported Projects' and my idea is for you to create a nice 'Word Cloud' of it similar to how I presented it in the ppt attached. Or it can be presented in some shape you'd think is nice. (search "word cloud" in Zarvix Pictures)

9) Call-to-Action. Make the 'Call-to-Action' panel of the brochure as "inviting" as possible.

10) Be creative. AGAIN. Aside for the copy points in the ppt guidelines attached, I would like to stress that you are free to edit/create whatever you deem fit to my vision. (as you've come to know what I'd like by now)

Don't forget to have fun!! It'll be awesome working with you.

**UPDATE in July 24: Use the PPT v2 for details, attached separately. (now with design pegs)**

**UPDATE in July 29: for the photos under 'First World Tech', please use the Cutter photo and Wire-drawing machine photo attached here.**

Hello again! Good job so far on the initial designs. To let you know what style I'd like our icons in "How We Serve You", please visit www.ironpeakph.folvane.com for our mock-up website.

You can also scroll down in the first page in "Our 4 Products" to see how I'd like our fonts to be used here so it'll be readable (i.e. through different font sizes, font effects like Bold & Italic)

As always, if you think you have a better idea on how to execute what I've mentioned above, go do it!

**UPDATE in July 24: Use the PPT v2 for the copy details, attached separately. Now with Design PEGS.**

Target Market(s)

Architectural firms. Building contractors. Steel wholesalers/distributors.

Industry/Entity Type

Real Estate

Requirements
Must have
• Simple. Approachable. Clear. Attractive. Uncluttered.
Should not have
• BULLET POINTS. (this shouldn't look like a Powerpoint material in any way or form)

```html
<!DOCTYPE html>
<html lang="en">
<head>
<meta charset="utf-8">
<title>Ironpeak Manufacturing Brochure</title>
<link rel="stylesheet" href="https://fonts.googleapis.com/css2?family=Open+Sans:ital,wght@0,400;0,600;0,700;1,400&display=swap">
<style>
  :root {
    --brand-blue: #3597cf;
    --charcoal: #4d4d4d;
    --paper: #ffffff;
    --quote-grey: #6b6b6b;
  }
  html, body {
    margin: 0;
    padding: 0;
    overflow: hidden;
    background: var(--paper);
  }
  .brochure {
    position: relative;
    width: 1200px;
    height: 855px;
    overflow: hidden;
    background: var(--paper);
    font-family: "Open Sans", Arial, sans-serif;
  }
  .backdrop {
    position: absolute;
    left: 0;
    top: 0;
  }
  .pill-heading {
    position: absolute;
    margin: 0;
    background: var(--paper);
    color: var(--brand-blue);
    font-weight: 700;
    font-size: 26px;
    letter-spacing: 0.6px;
    line-height: 1;
    padding: 3px 14px 5px;
    border-radius: 20px;
    white-space: nowrap;
  }
  .tag {
    position: absolute;
    background: var(--charcoal);
    color: var(--paper);
    font-weight: 600;
    font-size: 16px;
    letter-spacing: 0.5px;
    line-height: 1;
    padding: 6px 12px 7px;
    border-radius: 14px;
    white-space: nowrap;
  }
  .copy {
    position: absolute;
    color: var(--paper);
    font-weight: 700;
    font-size: 16.5px;
    letter-spacing: 0.5px;
    line-height: 22px;
    margin: 0;
    white-space: nowrap;
  }
  .lead {
    position: absolute;
    color: var(--paper);
    font-weight: 700;
    font-size: 19px;
    letter-spacing: 0.6px;
    line-height: 25px;
    margin: 0;
    white-space: nowrap;
  }
  .band-title {
    position: absolute;
    left: 102px;
    top: 355px;
    color: var(--paper);
    font-weight: 700;
    font-size: 39px;
    letter-spacing: 1.2px;
    line-height: 50px;
    margin: 0;
  }
  .band-mark {
    position: absolute;
    left: 470px;
    top: 390px;
    width: 125px;
    text-align: center;
    color: var(--charcoal);
    font-weight: 700;
    font-size: 24px;
    line-height: 1;
  }
  .cover-title {
    position: absolute;
    left: 674px;
    top: 82px;
    color: var(--brand-blue);
    font-weight: 400;
    font-size: 61px;
    letter-spacing: 1.4px;
    line-height: 74px;
    margin: 0;
    white-space: nowrap;
  }
  .cover-mark {
    position: absolute;
    left: 705px;
    top: 355px;
    width: 314px;
    text-align: center;
    color: var(--brand-blue);
    font-weight: 700;
    font-size: 46px;
    line-height: 1;
  }
  .tagline {
    position: absolute;
    left: 642px;
    top: 536px;
    color: var(--quote-grey);
    font-style: italic;
    font-size: 18px;
    letter-spacing: 0.6px;
    margin: 0;
    white-space: nowrap;
  }
  .overview {
    position: absolute;
    left: 642px;
    top: 584px;
    width: 466px;
    color: var(--paper);
    font-weight: 700;
    font-size: 20px;
    letter-spacing: 0.6px;
    line-height: 32px;
    text-align: right;
    margin: 0;
    white-space: nowrap;
  }
  .overview .brand-name {
    color: var(--brand-blue);
  }
</style>
</head>
<body>
<main class="brochure">
  <svg class="backdrop" width="1200" height="855" viewBox="0 0 1200 855" aria-hidden="true">
    <path d="M93 68 H652 V768 H93 A30 30 0 0 1 63 738 V98 A30 30 0 0 1 93 68 Z" fill="var(--brand-blue)"/>
    <rect x="600" y="225" width="558" height="300" fill="var(--brand-blue)"/>
    <rect x="1110" y="500" width="48" height="275" fill="var(--brand-blue)"/>
    <rect x="652" y="30" width="580" height="195" rx="30" fill="var(--paper)"/>
    <rect x="610" y="515" width="505" height="320" rx="30" fill="var(--paper)"/>
    <circle cx="862" cy="382" r="158" fill="var(--paper)"/>
    <rect x="33" y="332" width="577" height="150" fill="var(--charcoal)"/>
    <path d="M530 332 H610 V482 H530 A75 75 0 0 1 530 332 Z" fill="var(--paper)"/>
    <rect x="642" y="565" width="501" height="195" rx="26" fill="var(--charcoal)"/>
  </svg>

  <section class="panel-thinking">
    <h2 class="pill-heading" style="left:252px; top:84px;">Our Thinking</h2>
    <p class="lead" style="left:114px; top:119px;">&emsp;&emsp;&ensp;Your experience with our product matters,<br>every step of the way.</p>
    <span class="tag" style="left:104px; top:176px;">EASE TO BUILD</span>
    <p class="copy" style="left:116px; top:206px;">We believe in ease of construction using<br>uncompromising quality.</p>
    <span class="tag" style="left:104px; top:253px;">TRUTH IN PRODUCT</span>
    <p class="copy" style="left:118px; top:284px;">We only deliver products faithful to your terms.</p>
  </section>

  <section class="identity-band">
    <h1 class="band-title">IRONPEAK<br>Manufacturing</h1>
    <span class="band-mark">Ironpeak</span>
  </section>

  <section class="panel-service">
    <h2 class="pill-heading" style="left:212px; top:487px;">How We Serve You</h2>
    <span class="tag" style="left:106px; top:530px;">First World Tech</span>
    <p class="copy" style="left:126px; top:559px;">Italian. Danish. Chinese. We utilize first world<br>machines for first world quality products.</p>
    <span class="tag" style="left:106px; top:605px;">Honest Dimensions</span>
    <p class="copy" style="left:122px; top:633px;">We measure it in front of you with Gauge View.<br>What you want is what you’ll get.</p>
    <span class="tag" style="left:108px; top:677px;">2D Delivery</span>
    <p class="copy" style="left:120px; top:703px;">2 Days after-order delivery – 10 days return<br>allowance. We’ll call&nbsp; you if we’ll be late.</p>
  </section>

  <section class="panel-cover">
    <h1 class="cover-title">IRONPEAK<br>Manufacturing</h1>
    <span class="cover-mark">Ironpeak</span>
    <p class="tagline">“first-world standards to build the third-world up.”</p>
    <p class="overview"><span class="brand-name">Ironpeak</span> manufactures goods that<br>are first world in nature &amp; truth-telling in<br>class. Now you can build Sydney around<br>Taguig, Shanghai inside Binondo, and<br>Manhattan across Valero.</p>
  </section>
</main>
</body>
</html>
```